Tidal Oak Business Cards

We need something new, fun and exciting for business cards. Our current ones are just plain and we need a design that pops. We want name, position held, phone, email on the front, and a 20% discount on the back. I have also uploaded our old business cards creative to see what we are not wanting, and how boring they were and we want something jazzed up from this, cool design and catches people attention.

```html
<!DOCTYPE html>
<html lang="en">
<head>
<meta charset="utf-8">
<title>Tidal Oak Business Cards</title>
<link rel="stylesheet" href="https://fonts.googleapis.com/css2?family=Montserrat:wght@400;500;700;800&display=swap">
<style>
  :root {
    --backdrop: #e2e2e2;
    --navy: #173a69;
    --coral: #ea6e6e;
    --paper: #f4f4f4;
    --white: #ffffff;
  }
  * { margin: 0; padding: 0; box-sizing: border-box; }
  html, body {
    width: 1200px;
    height: 960px;
    overflow: hidden;
    background: var(--backdrop);
    font-family: "Montserrat", sans-serif;
  }
  .canvas { position: relative; width: 1200px; height: 960px; }

  .card {
    position: absolute;
    left: 305px;
    width: 602px;
    height: 344px;
    border-radius: 22px;
    overflow: hidden;
  }
  .card--back { top: 116px; background: var(--navy); }
  .card--front { top: 514px; background: var(--paper); }

  .card__decor { position: absolute; inset: 0; }

  .offer {
    position: absolute;
    left: 140px;
    top: 124px;
    width: 160px;
    text-align: center;
    line-height: 1;
  }
  .offer__value {
    display: block;
    color: var(--white);
    font-weight: 800;
    font-size: 46px;
    letter-spacing: -1px;
  }
  .offer__label {
    display: block;
    margin-top: 8px;
    color: var(--coral);
    font-weight: 800;
    font-size: 26px;
  }

  .brand {
    position: absolute;
    left: 62px;
    top: 130px;
    display: flex;
    align-items: center;
    gap: 8px;
  }
  .brand__dot {
    width: 14px;
    height: 14px;
    border-radius: 50%;
    background: var(--coral);
  }
  .brand__name {
    color: var(--navy);
    font-weight: 700;
    font-size: 27px;
    letter-spacing: -0.5px;
  }

  .person {
    position: absolute;
    right: 36px;
    top: 58px;
    text-align: right;
  }
  .person__name {
    color: var(--navy);
    font-weight: 500;
    font-size: 22px;
  }
  .person__name strong { font-weight: 800; }
  .person__role {
    margin-top: 2px;
    color: var(--coral);
    font-size: 15px;
  }

  .contact {
    position: absolute;
    right: 36px;
    top: 255px;
    list-style: none;
    text-align: right;
    color: var(--navy);
    font-size: 15.5px;
    line-height: 21px;
  }
  .contact__item { display: flex; justify-content: flex-end; align-items: center; gap: 6px; }
  .contact__icon { width: 14px; height: 14px; fill: var(--coral); }
</style>
</head>
<body>
<main class="canvas">

  <section class="card card--back" aria-label="Card back: discount offer">
    <svg class="card__decor" viewBox="0 0 602 344" role="img" aria-label="Decorative coral ring">
      <circle cx="225" cy="175" r="170" fill="none" stroke="var(--coral)" stroke-width="58"/>
    </svg>
    <p class="offer">
      <span class="offer__value">20%</span>
      <span class="offer__label">DISCOUNT</span>
    </p>
  </section>

  <section class="card card--front" aria-label="Card front: contact details">
    <svg class="card__decor" viewBox="0 0 602 344" role="img" aria-label="Navy band with coral ring framing the company name">
      <rect x="0" y="0" width="225" height="344" fill="var(--navy)"/>
      <circle cx="140" cy="150" r="148" fill="var(--paper)" stroke="var(--coral)" stroke-width="58"/>
    </svg>

    <div class="brand">
      <span class="brand__dot"></span>
      <span class="brand__name">Tidal Oak</span>
    </div>

    <div class="person">
      <p class="person__name"><strong>Daniel</strong> Reyes</p>
      <p class="person__role">Owner</p>
    </div>

    <ul class="contact">
      <li class="contact__item">(123) 456-7890
        <svg class="contact__icon" viewBox="0 0 24 24" aria-hidden="true"><path d="M6.6 10.8a15.1 15.1 0 0 0 6.6 6.6l2.2-2.2a1 1 0 0 1 1-.25 11.4 11.4 0 0 0 3.6.57 1 1 0 0 1 1 1V20a1 1 0 0 1-1 1A17 17 0 0 1 3 4a1 1 0 0 1 1-1h3.5a1 1 0 0 1 1 1c0 1.25.2 2.45.57 3.57a1 1 0 0 1-.25 1z"/></svg>
      </li>
      <li class="contact__item">daniel@tidaloak.com
        <svg class="contact__icon" viewBox="0 0 24 24" aria-hidden="true"><path d="M2 5h20v14H2zm2 2v.5l8 5 8-5V7zm0 2.8V17h16V9.8l-8 5z"/></svg>
      </li>
    </ul>
  </section>

</main>
</body>
</html>
```